Masonry and Landscaping Construction company business card

Looking for a business card design for a construction company named Ferrano Construction. It is an italian-american family business that specializes in custom stone work, patios, walkways, driveways, steps, outdoor kitchens, concrete, waterproofing, power wash, landscaping and more. Our colors are mostly red and white with some black. We're looking for a bold design. we also like to incorporate a picture of my family's hometown somewhere in it.
Target Market(s)
Luxury home owners
Industry/Entity Type
Construction
Contact Information for Business Card
Details includes should be bullet points mentioning the services provided. Custom Stone Work, Outdoor Kitchens, Fire Pits, Patios, Walkways, Steps, Concrete, Waterproofing, powerwash and landscaping
Requirements
Must have
- Would like a spot on the card for co-owners names, numbers and email to be listed also looking to add the QR code for an instagram page
Nice to have
- would like something bold, based around the colors red and white with black outlines or details

```html
<!DOCTYPE html>
<html lang="en">
<head>
<meta charset="utf-8">
<title>Ferrano Construction – Business Card</title>
<link href="https://fonts.googleapis.com/css2?family=Exo+2:wght@500;600;700;800&display=swap" rel="stylesheet">
<style>
  :root {
    --stage: #e8e5e0;
    --carbon: #232323;
    --ink: #0b0b0b;
    --brand-red: #d10a1e;
    --white: #ffffff;
    --tick-red: #e3142a;
    --stone: #9a8a74;
    --hill: #5f7f47;
    --sky: #a9b1b4;
  }
  * { box-sizing: border-box; margin: 0; padding: 0; }
  html, body {
    width: 1189px; height: 1200px; overflow: hidden;
    background: var(--stage);
    font-family: "Exo 2", sans-serif;
  }
  .card {
    position: absolute; left: 94px; width: 1000px; height: 568px;
    border-radius: 34px; overflow: hidden;
    box-shadow: 0 10px 26px rgba(0,0,0,.28);
  }
  .card--front { top: 20px; background: var(--carbon); }
  .card--back { top: 612px; background: var(--ink); }

  /* front */
  .front-bands { position: absolute; inset: 0; width: 100%; height: 100%; }
  .brand-mark {
    position: absolute; left: 0; right: 0; top: 150px;
    display: flex; align-items: center; justify-content: center; gap: 16px;
    color: var(--white); font-weight: 800; font-size: 52px;
    letter-spacing: 1px; text-transform: uppercase;
  }
  .brand-mark .mark-square { width: 34px; height: 34px; background: var(--brand-red); }
  .contact-phone {
    position: absolute; left: 52px; top: 490px;
    display: flex; align-items: center; gap: 20px;
    color: var(--white); font-size: 38px; font-weight: 600; letter-spacing: 1px;
  }
  .contact-phone svg { width: 26px; height: 36px; }
  .contact-person {
    position: absolute; right: 36px; top: 448px; text-align: right; color: var(--white);
  }
  .contact-person .name { font-size: 40px; font-weight: 600; letter-spacing: 2px; line-height: 1.1; text-transform: uppercase; }
  .contact-person .email { font-size: 27px; font-weight: 500; letter-spacing: 1px; margin-top: 4px; }

  /* back */
  .hometown-photo {
    position: absolute; left: 330px; top: 0; right: 0; bottom: 0;
    background: linear-gradient(180deg, var(--sky) 0%, #7d9170 18%, var(--hill) 38%, #8c7a62 60%, var(--stone) 78%, #55703e 100%);
  }
  .photo-fade {
    position: absolute; left: 320px; top: 0; width: 380px; height: 100%;
    background: linear-gradient(90deg, var(--ink) 0%, rgba(11,11,11,.75) 45%, rgba(11,11,11,0) 100%);
  }
  .services-banner {
    position: absolute; left: 0; top: 60px; width: 342px; height: 48px;
    background: var(--brand-red);
    clip-path: polygon(0 0, 100% 0, 94% 100%, 0 100%);
    color: var(--white); font-size: 27px; font-weight: 700; letter-spacing: 1px;
    padding-left: 54px; line-height: 48px; text-transform: uppercase;
  }
  .services-list {
    position: absolute; left: 56px; top: 134px; list-style: none;
    color: var(--white); font-size: 23px; font-weight: 600; letter-spacing: 1.5px;
    text-transform: uppercase;
  }
  .services-list li { display: flex; align-items: center; gap: 20px; height: 30px; }
  .services-list svg { width: 20px; height: 20px; flex: none; }
  .back-brand {
    position: absolute; left: 60px; top: 458px;
    color: var(--white); font-weight: 800; font-size: 40px; letter-spacing: 1px;
    text-transform: uppercase; line-height: 1.05;
  }
</style>
</head>
<body>

<section class="card card--front">
  <svg class="front-bands" viewBox="0 0 1000 568" preserveAspectRatio="none" aria-hidden="true">
    <path d="M0 308 Q500 228 1000 308 L1000 568 L0 568 Z" fill="var(--white)"/>
    <path d="M0 386 Q500 316 1000 386 L1000 568 L0 568 Z" fill="var(--brand-red)"/>
  </svg>
  <div class="brand-mark"><span class="mark-square"></span>Ferrano Construction</div>
  <div class="contact-phone">
    <svg viewBox="0 0 26 36" aria-hidden="true"><path d="M6 2 L11 10 L8 13 Q9 21 15 26 L18 23 L23 30 L18 34 Q4 28 2 8 Z" fill="var(--white)"/></svg>
    (555)010 2047
  </div>
  <div class="contact-person">
    <div class="name">Marco Bellini</div>
    <div class="email">info@ferranobuild.com</div>
  </div>
</section>

<section class="card card--back">
  <div class="hometown-photo" role="img" aria-label="Photograph of the family's Italian hometown: stone bell tower and old town houses beneath green mountains"></div>
  <div class="photo-fade"></div>
  <div class="services-banner">Our Services</div>
  <ul class="services-list">
    <li><svg viewBox="0 0 20 20"><path d="M2 11 L8 17 L18 3" fill="none" stroke="var(--tick-red)" stroke-width="4"/></svg>Custom Stone Work</li>
    <li><svg viewBox="0 0 20 20"><path d="M2 11 L8 17 L18 3" fill="none" stroke="var(--tick-red)" stroke-width="4"/></svg>Outdoor Kitchens</li>
    <li><svg viewBox="0 0 20 20"><path d="M2 11 L8 17 L18 3" fill="none" stroke="var(--tick-red)" stroke-width="4"/></svg>Fire Pits</li>
    <li><svg viewBox="0 0 20 20"><path d="M2 11 L8 17 L18 3" fill="none" stroke="var(--tick-red)" stroke-width="4"/></svg>Patios</li>
    <li><svg viewBox="0 0 20 20"><path d="M2 11 L8 17 L18 3" fill="none" stroke="var(--tick-red)" stroke-width="4"/></svg>Walkways</li>
    <li><svg viewBox="0 0 20 20"><path d="M2 11 L8 17 L18 3" fill="none" stroke="var(--tick-red)" stroke-width="4"/></svg>Steps</li>
    <li><svg viewBox="0 0 20 20"><path d="M2 11 L8 17 L18 3" fill="none" stroke="var(--tick-red)" stroke-width="4"/></svg>Concrete</li>
    <li><svg viewBox="0 0 20 20"><path d="M2 11 L8 17 L18 3" fill="none" stroke="var(--tick-red)" stroke-width="4"/></svg>Waterproofing</li>
    <li><svg viewBox="0 0 20 20"><path d="M2 11 L8 17 L18 3" fill="none" stroke="var(--tick-red)" stroke-width="4"/></svg>Powerwash and Landscaping</li>
  </ul>
  <div class="back-brand">Ferrano<br>Construction</div>
</section>

</body>
</html>
```